Say "Velvet Crumb"! Cheesecakes that is. Needs a Web Design

Velvet Crumb LLC is a start up company based in Pickerington, Ohio. We make New York Style Cheesecakes that everyone will love. We want to start building our brand with a website that will inform the the community. Lets let them know the many mouthwatering flavors of cheesecake there are to enjoy and the 3 sizes you can dive in. Because we are small, we will only be serving locally in the Franklin and Fairfield counties. We would like to see a web design using the colors from our logo. The finished design should display a playful theme and portray comfort, desire, indulgence, and fulfillment.

Target Market(s)

Dessert Lovers

Industry/Entity Type

Food Store

Coding

Coded - Design and coding required

Number of Pages Required

5+ page

Requirements
Must have
• Everything I asked for on my web format page
Nice to have
• Colors similar to the logo

```html
<!DOCTYPE html>
<html lang="en">
<head>
<meta charset="utf-8">
<title>Velvet Crumb — New York Style Cheesecakes</title>
<link href="https://fonts.googleapis.com/css2?family=Courgette&family=Open+Sans:wght@400;600;700&display=swap" rel="stylesheet">
<style>
:root{
  --red:#b2262b;
  --red-deep:#8f1c21;
  --script-red:#a8232a;
  --orange:#f7a11d;
  --heading-orange:#e0861a;
  --cream:#fcd78f;
  --cream-soft:#fde9b8;
  --panel:#efefef;
  --dark:#2a2a2a;
  --ink:#4a4a4a;
  --white:#ffffff;
  --muted:#9a9a9a;
}
*{box-sizing:border-box;margin:0;padding:0}
html,body{width:1200px;height:2335px;overflow:hidden}
body{position:relative;background:var(--white);font-family:"Open Sans",Arial,sans-serif;color:var(--ink)}
.abs{position:absolute}
.script{font-family:"Courgette",cursive}
.btn{position:absolute;background:var(--orange);color:var(--white);font-size:11px;font-weight:600;text-transform:uppercase;display:flex;align-items:center;justify-content:center;letter-spacing:.3px}

/* hero */
.hero{left:0;top:0;width:1200px;height:560px;background:radial-gradient(ellipse at 70% 40%,#6b4a35 0%,#3a2418 45%,#1a100b 100%)}
.ribbon{left:101px;top:72px;width:996px;height:49px;background:var(--red);clip-path:polygon(0 0,100% 0,97% 50%,100% 100%,0 100%,3% 50%)}
.nav{right:154px;top:72px;height:49px;display:flex;align-items:center;gap:29px;color:var(--white);font-size:15px}
.nav svg{margin-left:12px}
.badge{left:156px;top:0;width:124px;height:230px;background:var(--white);clip-path:polygon(0 0,100% 0,100% 100%,50% 88%,0 100%)}
.badge-mark{left:133px;top:6px;width:170px;height:170px;border-radius:50%;background:var(--white);display:flex;align-items:center;justify-content:center;text-align:center;color:var(--red);font-weight:700;font-size:25px;line-height:1.1}
.hero-cake{left:257px;top:210px;width:295px;height:285px;border-radius:50%;background:radial-gradient(circle at 50% 40%,#f5eadc 0%,#c9a07a 45%,#8c2a25 70%,#10201a 100%)}
.hero-title{left:654px;top:252px;font-size:46px;color:var(--white)}
.hero-text{left:654px;top:326px;width:325px;font-size:11.5px;line-height:1.42;color:#f2e9e2}
.hero .btn{left:657px;top:408px;width:103px;height:35px}
.arrow{top:323px}

/* about */
.about-card{left:120px;top:598px;width:415px;height:295px;border:1px solid #dedede;background:var(--white);box-shadow:0 1px 3px rgba(0,0,0,.08)}
.about-strip{left:135px;top:615px;width:83px;height:264px;background:var(--cream)}
.about-strip-text{left:135px;top:615px;width:83px;height:264px;display:flex;align-items:center;justify-content:center}
.about-strip-text p{transform:rotate(-90deg);white-space:nowrap;text-align:center;line-height:1.05;font-size:27px}
.about-strip-text .brand{color:var(--heading-orange)}
.about-strip-text .sub{color:var(--script-red)}
.about-photo{left:218px;top:615px;width:303px;height:264px;background:linear-gradient(160deg,#f7c640 0%,#f4e7c9 55%,#c98e4f 85%,#5a3a22 100%)}
.about-title{left:559px;top:606px;font-size:34px;color:var(--heading-orange)}
.about-text{left:559px;top:665px;width:530px;font-size:11.5px;line-height:1.42;color:var(--ink)}
.about-quote{left:559px;top:762px;font-size:15.5px;color:var(--script-red)}
.about .btn{left:559px;top:811px;width:103px;height:37px}

/* cakes */
.section-title{width:1200px;left:0;text-align:center;color:var(--script-red)}
.cakes-title{top:940px;font-size:36px}
.cakes-panel{left:123px;top:996px;width:954px;height:241px;background:var(--panel);border:1px solid #e2e2e2}
.cake-card{top:1015px;width:220px;height:203px;background:var(--cream);padding:6px}
.cake-card.active{background:var(--red)}
.cake-photo{width:208px;height:151px;background:var(--white);display:flex;align-items:center;justify-content:center}
.cake-photo span{display:block;width:170px;height:128px;border-radius:50%}
.cake-name{text-align:center;font-size:17px;color:#2b2b2b;margin-top:12px}
.cake-card.active .cake-name{color:var(--white)}

/* blog */
.blog{left:123px;top:1254px;width:954px;height:430px;background:linear-gradient(180deg,#3a3530 0%,#262626 35%,#262626 100%)}
.blog-title{top:1288px;font-size:33px;color:var(--white)}
.post{top:1382px;width:208px}
.post-photo{width:208px;height:194px}
.post-title{margin-top:14px;font-size:13.5px;color:var(--white)}
.post-text{margin-top:4px;font-size:10.5px;line-height:1.38;color:#e6e6e6}

/* newsletter */
.newsletter{left:0;top:1713px;width:1200px;height:307px;background:linear-gradient(90deg,#b2484a 0%,#a33a3d 45%,#c06a6c 70%,#9e3639 100%)}
.news-title{top:1782px;font-size:33px;color:var(--white)}
.email{left:279px;top:1858px;width:432px;height:54px;background:rgba(255,255,255,.2);color:var(--white);font-size:21px;display:flex;align-items:center;padding-left:27px}
.subscribe{left:724px;top:1858px;width:197px;height:54px;background:var(--orange);color:var(--white);font-size:23px;font-weight:700;display:flex;align-items:center;justify-content:center}

/* footer */
.footer{left:0;top:2020px;width:1200px;height:315px;background:var(--dark)}
.footer-mark{left:0;width:1200px;top:2050px;text-align:center;color:#8d8d8d;font-weight:700;font-size:21px;line-height:1.1}
.footer-nav{left:0;width:1200px;top:2160px;display:flex;justify-content:center;gap:37px;color:#e4e4e4;font-size:15px}
.social{left:0;width:1200px;top:2206px;display:flex;justify-content:center;gap:17px}
.address{left:0;width:1200px;top:2258px;text-align:center;font-size:11.5px;color:#a0a0a0}
.copy{left:0;width:1200px;top:2290px;text-align:center;font-size:9.5px;color:#a0a0a0}
</style>
</head>
<body>

<header class="hero abs" role="img" aria-label="Blurred warm bakery interior behind the featured cheesecake"></header>
<div class="ribbon abs"></div>
<div class="badge abs"></div>
<div class="badge-mark abs">Velvet<br>Crumb</div>
<nav class="nav abs">
  <span>Home</span><span>Flavor</span><span>Catering</span><span>Delivery</span><span>Q/A</span><span>Contact</span>
  <svg width="14" height="14" viewBox="0 0 14 14" aria-label="Search"><circle cx="5.5" cy="5.5" r="4" fill="none" stroke="#fff" stroke-width="2"/><line x1="8.5" y1="8.5" x2="13" y2="13" stroke="#fff" stroke-width="2"/></svg>
</nav>
<div class="hero-cake abs" role="img" aria-label="Banana split cheesecake with whipped cream, chocolate drizzle, nuts and a cherry on a dark plate"></div>
<h1 class="hero-title abs script">Banana Split</h1>
<p class="hero-text abs">Duis aute irure dolor in reprehenderit in voluptate velit esse cillum dolore eu fugiat nulla pariatur. Excepteur sint occaecat cupidatat non proident, sunt in culpa qui officia deserunt mollit anim id est laborum</p>
<div class="hero"><span class="btn">Learn More</span></div>
<svg class="abs arrow" style="left:136px" width="36" height="76" viewBox="0 0 36 76" aria-label="Previous slide"><polyline points="34,2 2,38 34,74" fill="none" stroke="#fff" stroke-width="1.5"/></svg>
<svg class="abs arrow" style="left:1045px" width="36" height="76" viewBox="0 0 36 76" aria-label="Next slide"><polyline points="2,2 34,38 2,74" fill="none" stroke="#fff" stroke-width="1.5"/></svg>

<section class="about">
  <div class="about-card abs"></div>
  <div class="about-strip abs"></div>
  <div class="about-strip-text abs"><p class="script"><span class="brand">Velvet Crumb</span><br><span class="sub">Philosophy</span></p></div>
  <div class="about-photo abs" role="img" aria-label="Slice of peach cheesecake with golden glaze on a graham crust"></div>
  <h2 class="about-title abs script">Velvet Crumb</h2>
  <p class="about-text abs">At Velvet Crumb we strive to provide our customers with a food product that satisfies their greatest indulgence. Velvet Crumb takes a particular approach to preparing one of America's favorite desserts. Cheesecake is beautiful in nature, so we put a greater emphasis on substance. We don't use a lot of bells and whistles, but we do add enough bold flavors to pleasure everyone's palate</p>
  <p class="about-quote abs script">Velvet Crumb is simple, made with a complex human need "Love".</p>
  <span class="btn">Learn More</span>
</section>

<section class="cakes">
  <h2 class="section-title cakes-title abs script">Cakes</h2>
  <div class="cakes-panel abs"></div>
  <div class="cake-card active abs" style="left:140px"><div class="cake-photo"><span role="img" aria-label="Lemon blueberry cheesecake" style="background:radial-gradient(circle at 50% 40%,#5a1330 0%,#e9e2c0 60%,#1b1b1b 80%,#fff 81%)"></span></div><p class="cake-name script">Lemonblueberry</p></div>
  <div class="cake-card abs" style="left:373px"><div class="cake-photo"><span role="img" aria-label="Maple bacon cheesecake" style="background:radial-gradient(circle at 50% 40%,#b97a45 0%,#c98d55 60%,#1b1b1b 80%,#fff 81%)"></span></div><p class="cake-name script">Maplebacon</p></div>
  <div class="cake-card abs" style="left:607px"><div class="cake-photo"><span role="img" aria-label="Peanut butter cheesecake" style="background:radial-gradient(circle at 50% 40%,#4a2c18 0%,#e6d2a8 55%,#1b1b1b 80%,#fff 81%)"></span></div><p class="cake-name script">Peanutbutter</p></div>
  <div class="cake-card abs" style="left:840px"><div class="cake-photo"><span role="img" aria-label="White chocolate raspberry cheesecake" style="background:radial-gradient(circle at 50% 40%,#d2233a 0%,#f0ecd8 50%,#1b1b1b 80%,#fff 81%)"></span></div><p class="cake-name script">Whitechocolateraspberry</p></div>
</section>

<section>
  <div class="blog abs" role="img" aria-label="Dim café table background"></div>
  <h2 class="section-title blog-title abs script">Blog and Testimonials</h2>
  <article class="post abs" style="left:151px"><div class="post-photo" role="img" aria-label="Layered tiramisu cake topped with a strawberry" style="background:linear-gradient(180deg,#fbfbfb 0%,#eadcc6 45%,#8a5a34 80%,#f4f4f4 100%)"></div><h3 class="post-title script">Temporibus autem quibusdam</h3><p class="post-text">Neque porro quisquam est, qui dolorem ipsum quia dolor sit amet, consectetur, adipisci velit, sed quia non numquam</p></article>
  <article class="post abs" style="left:380px"><div class="post-photo" role="img" aria-label="Rice pudding in a red pot on a wooden board" style="background:linear-gradient(160deg,#6e4a30 0%,#eae3d2 45%,#9a2a22 70%,#7a5334 100%)"></div><h3 class="post-title script">Temporibus autem quibusdam</h3><p class="post-text">Neque porro quisquam est, qui dolorem ipsum quia dolor sit amet, consectetur, adipisci velit, sed quia non numquam</p></article>
  <article class="post abs" style="left:609px"><div class="post-photo" role="img" aria-label="Berry-topped cheesecake with red sauce" style="background:linear-gradient(180deg,#9fc4d8 0%,#d6304a 35%,#f3ead8 65%,#f5f5f5 100%)"></div><h3 class="post-title script">Temporibus autem quibusdam</h3><p class="post-text">Neque porro quisquam est, qui dolorem ipsum quia dolor sit amet, consectetur, adipisci velit, sed quia non numquam</p></article>
  <article class="post abs" style="left:840px"><div class="post-photo" role="img" aria-label="Slice of caramel chocolate cheesecake on a white plate" style="background:linear-gradient(180deg,#f4f4f4 0%,#8a5a2e 35%,#ecdcc0 60%,#f6f6f6 100%)"></div><h3 class="post-title script">Temporibus autem quibusdam</h3><p class="post-text">Neque porro quisquam est, qui dolorem ipsum quia dolor sit amet, consectetur, adipisci velit, sed quia non numquam</p></article>
</section>

<section>
  <div class="newsletter abs" role="img" aria-label="Pink-tinted photo of a white frosted cake with roses"></div>
  <h2 class="section-title news-title abs script">Get Daily Specials from our newsletter</h2>
  <div class="email abs">Your Email</div>
  <div class="subscribe abs">Subscribe</div>
</section>

<footer>
  <div class="footer abs"></div>
  <div class="footer-mark abs">Velvet<br>Crumb</div>
  <nav class="footer-nav abs"><span>Home</span><span>Flavor</span><span>Catering</span><span>Delivery</span><span>Q/A</span><span>Contact</span></nav>
  <div class="social abs">
    <svg width="38" height="38" viewBox="0 0 38 38" aria-label="Social link"><rect x="7" y="7" width="24" height="24" transform="rotate(45 19 19)" fill="none" stroke="#fff" stroke-width="1.2"/></svg>
    <svg width="38" height="38" viewBox="0 0 38 38" aria-label="Social link"><rect x="7" y="7" width="24" height="24" transform="rotate(45 19 19)" fill="none" stroke="#fff" stroke-width="1.2"/></svg>
    <svg width="38" height="38" viewBox="0 0 38 38" aria-label="Social link"><rect x="7" y="7" width="24" height="24" transform="rotate(45 19 19)" fill="none" stroke="#fff" stroke-width="1.2"/></svg>
    <svg width="38" height="38" viewBox="0 0 38 38" aria-label="Social link"><rect x="7" y="7" width="24" height="24" transform="rotate(45 19 19)" fill="none" stroke="#fff" stroke-width="1.2"/></svg>
  </div>
  <p class="address abs">415 Orchard Row Ste 210 &nbsp;|&nbsp; Lancaster &nbsp;|&nbsp; OH 43130-2201</p>
  <p class="copy abs">© 2015 • www.velvetcrumb.com • PRIVACY POLICY</p>
</footer>

</body>
</html>
```